A5 Flyer for Financial Services Business

I am after a re-design of our business flyer to fit in with our new branding style and logo colour scheme. Wanting something with a bit of designer flair that I could not create myself. I have included the flyer which I created which lacks style so dazzle me.

I want to use the same content.

Text for main body of flyer is

Are you a small business owner, tradie or PAVC Service Provider struggling to stay on top of your bookkeeping and compliance obligations? If so we would love to help you get back on track and take control of your business finances so that you can make informed business decisions and focus on what you do best.

We have over 20 years industry experience and, as a small business ourselves, we are able to offer our clients a personal bookkeeping solution tailored to meet the needs of your business.

Accounts Payable | Accounts Receivable
Customer Invoicing
Bank and Credit Card Reconciliations
Payroll | Superannuation | Payroll Tax
Business Activity | Instalment Activity Statements
Regular Financial Reports
Ledgerly and Tallybook Set-Up and Training

```html
<!DOCTYPE html>
<html lang="en">
<head>
<meta charset="utf-8">
<title>Even Keel Financial Services – Bookkeeping Flyer</title>
<link href="https://fonts.googleapis.com/css2?family=Montserrat:wght@400;600;800&family=Open+Sans:wght@300;400&display=swap" rel="stylesheet">
<style>
  :root{
    --teal:#0e978c;
    --teal-dark:#0b7f76;
    --teal-deep:#086a63;
    --navy:#0b3a52;
    --paper:#ececec;
    --ink:#2e2e2e;
    --grey-text:#444;
    --backdrop:#6b6b6b;
    --white:#ffffff;
  }
  *{margin:0;padding:0;box-sizing:border-box}
  html,body{width:694px;height:1200px;overflow:hidden}
  body{background:var(--backdrop);position:relative;font-family:"Open Sans",Arial,sans-serif}
  .flyer{position:absolute;left:0;top:110px;width:711px;height:1005px;background:var(--paper);
    transform:scale(0.9761);transform-origin:top left;overflow:hidden}
  .hero-photo{position:absolute;left:0;top:0;width:711px;height:318px;
    background:radial-gradient(ellipse at 68% 60%, #b98a5c 0 14%, transparent 28%),
      linear-gradient(180deg,#5d7280 0%,#7d8d95 45%,#5b6b73 72%,#2b3136 78%,#24292d 100%)}
  .hero-shapes{position:absolute;left:0;top:0}
  .brand{position:absolute;left:26px;top:222px;display:flex;align-items:center;gap:8px;
    font-family:"Open Sans",Arial,sans-serif;font-weight:400;color:var(--teal-dark);font-size:17px;line-height:1.05}
  .brand-mark{width:14px;height:14px;background:var(--teal-dark)}
  .headline{position:absolute;right:26px;top:357px;text-align:right}
  .headline h1{font-family:"Montserrat",Arial,sans-serif;font-weight:800;font-size:37px;color:var(--navy);letter-spacing:0.5px;line-height:1}
  .headline p{font-family:"Montserrat",Arial,sans-serif;font-weight:400;font-size:22px;letter-spacing:4.6px;color:var(--grey-text);margin-top:4px;margin-right:-4px}
  .intro{position:absolute;left:26px;top:470px;width:659px;font-size:15.6px;line-height:19.6px;color:var(--ink);text-align:justify}
  .intro p+p{margin-top:15px}
  .services-title{position:absolute;left:29px;top:672px;font-family:"Montserrat",Arial,sans-serif;font-weight:600;font-size:23.5px;color:var(--navy)}
  .service-list{position:absolute;list-style:none;font-size:16px;color:var(--ink)}
  .service-list li{position:relative;padding-left:15px}
  .service-list li::before{content:"";position:absolute;left:-1px;top:6px;width:12px;height:12px;border-radius:50%;background:var(--teal)}
  .service-list li:not(:last-child)::after{content:"";position:absolute;left:4px;top:19px;width:3px;height:14px;
    background:repeating-linear-gradient(180deg,var(--teal) 0 5px,transparent 5px 7px)}
  .services-left{left:35px;top:719px}
  .services-left li{margin-bottom:14px;line-height:19.5px}
  .services-right{left:360px;top:722px}
  .services-right li{margin-bottom:12px;line-height:20px}
  .accreditation{position:absolute;left:465px;top:838px;width:246px;height:50px;background:var(--teal);
    color:var(--white);font-size:19px;line-height:25px;padding:0 0 0 12px;font-weight:300}
  .contact-band{position:absolute;left:0;top:922px;width:711px;height:83px;background:var(--teal);color:var(--white)}
  .contact-band .label{position:absolute;left:150px;top:14px;font-family:"Montserrat",Arial,sans-serif;font-weight:600;font-size:15px}
  .contact-band .phone{position:absolute;left:375px;top:4px;font-family:"Montserrat",Arial,sans-serif;font-weight:600;font-size:27px;letter-spacing:0.5px}
  .contact-band .web{position:absolute;left:150px;top:36px;font-size:19px;letter-spacing:0.2px}
</style>
</head>
<body>
<article class="flyer">
  <div class="hero-photo" role="img" aria-label="Photo of a glass jar filled with coins with a green seedling growing from it, on a blue-grey textured backdrop"></div>
  <svg class="hero-shapes" width="711" height="345" viewBox="0 0 711 345" aria-hidden="true">
    <polygon points="0,185 268,185 272,190 0,190" fill="var(--teal)"/>
    <polygon points="0,190 272,190 226,273 0,273" fill="var(--white)"/>
    <polygon points="0,273 226,273 171,338 0,338" fill="var(--teal)"/>
    <polygon points="266,186 356,338 171,338" fill="var(--teal-dark)"/>
    <polygon points="356,338 455,318 711,318 711,345 340,345" fill="var(--paper)"/>
    <polygon points="330,330 455,318 356,338" fill="var(--teal-deep)"/>
  </svg>
  <div class="brand"><span class="brand-mark"></span><span>EVEN KEEL<br>Financial Services</span></div>

  <header class="headline">
    <h1>BOOKKEEPING TAILORED</h1>
    <p>TO YOUR BUSINESS NEEDS</p>
  </header>

  <section class="intro">
    <p>Are you a small business owner, tradie or PAVC Service Provider struggling to stay on top of your bookkeeping and compliance obligations? If so we would love to help you get back on track and take control of your business finances so that you can make informed business decisions and focus on what you do best.</p>
    <p>We have over 20 years industry experience and, as a small business ourselves, we are able to offer our clients a personal bookkeeping solution tailored to meet the needs of your business.</p>
  </section>

  <h2 class="services-title">SERVICES WE PROVIDE</h2>
  <ul class="service-list services-left">
    <li>Accounts Payable | Accounts Receivable</li>
    <li>Customer Invoicing</li>
    <li>Bank and Credit Card Reconciliations</li>
    <li>Business Activity | Instalment Activity<br>Statements</li>
  </ul>
  <ul class="service-list services-right">
    <li>Payroll | Superannuation | Payroll Tax</li>
    <li>Regular Financial Reports</li>
    <li>Ledgerly and Tallybook Set-Up and Training</li>
  </ul>

  <div class="accreditation">Ledgerly Certified Advisor<br>Tallybook Pro Advisor</div>

  <footer class="contact-band">
    <span class="label">FOR MORE INFO</span>
    <span class="phone">0400 555 019</span>
    <span class="web">www.evenkeelfinancial.example.com.au</span>
  </footer>
</article>
</body>
</html>
```